Need Web Design for Business Process Outsourcing Company (Korvenza)

Korvenza is a business process outsourcing company. Need a simple site similar to http://www.taskmeridianhub.com/ but with a more professional and credible look. New to the process; not sure where to start and comparing my options. Please let me know what my options are if I choose to go with you. Logo is attached for your reference. Please use same colorway

Reason: I want the final product to be coded. Please confirm you will be able to code final design.

Industry/Entity Type

Business

Coding

Coded - Design and coding required

```html
<!DOCTYPE html>
<html lang="en">
<head>
<meta charset="utf-8">
<title>Korvenza – Outsourcing Business Services</title>
<link href="https://fonts.googleapis.com/css2?family=Oswald:wght@500;600&family=Raleway:wght@400;500&family=Roboto:wght@400;500;700&display=swap" rel="stylesheet">
<style>
:root{
  --blue:#1a92d2;
  --blue-dark:#0c5e94;
  --navy:#0b3f66;
  --ink:#1e1e1e;
  --black:#050505;
  --grey:#6d6d6d;
  --light:#f3f5f7;
  --line:#d5dbe0;
  --white:#ffffff;
}
*{margin:0;padding:0;box-sizing:border-box}
html,body{width:1200px;height:4813px;overflow:hidden}
body{font-family:'Roboto',Arial,sans-serif;color:var(--ink);background:var(--white);position:relative}
.section{position:absolute;left:0;width:1200px;overflow:hidden}
.abs{position:absolute}
.title{font-family:'Raleway',Arial,sans-serif;font-weight:400;text-align:center;font-size:38px;color:var(--ink)}
.title span{color:var(--blue)}
.link-more{font-size:15px;letter-spacing:1px;color:var(--blue);font-weight:500}
/* header */
.site-header{top:0;height:116px}
.brand{left:78px;top:24px;display:flex;align-items:center;gap:14px}
.brand-square{width:62px;height:62px;background:var(--blue-dark)}
.brand-name{font-family:'Roboto',sans-serif;font-weight:700;font-size:44px;color:var(--blue-dark)}
.top-links{left:484px;top:10px;display:flex;gap:34px;font-size:16px;color:#333;align-items:center}
.top-links .ico{display:inline-block;vertical-align:middle;margin-left:8px}
.socials{display:flex;gap:14px}
.socials i{display:block;width:36px;height:36px;border-radius:50%;background:var(--blue)}
.site-header .socials{left:934px;top:56px}
.site-header .socials i:last-child{background:#9a9a9a}
/* nav */
.main-nav{top:116px;height:64px;background:var(--blue);display:flex;padding-left:78px}
.main-nav a{color:var(--white);text-decoration:none;font-size:16px;text-transform:uppercase;line-height:64px;padding:0 21px}
.main-nav a.active{background:#2b2b2b}
/* hero */
.hero{top:180px;height:574px}
.hero-photo{inset:0;background:linear-gradient(180deg,#f4f5f6 0%,#e2e6ea 45%,#b9c1c8 75%,#8b969f 100%)}
.hero h1{left:78px;top:112px;font-family:'Oswald',sans-serif;font-weight:600;font-size:92px;line-height:1;color:#1a1a1a;letter-spacing:1px}
.hero h2{left:78px;top:222px;font-family:'Oswald',sans-serif;font-weight:500;font-size:46px;color:#1a1a1a}
.btn-blue{background:var(--blue);color:var(--white);font-size:19px;text-transform:uppercase;display:flex;align-items:center;justify-content:center}
.hero .btn-blue{left:78px;top:306px;width:222px;height:62px}
/* welcome */
.welcome{top:754px;height:417px;background:var(--black);color:var(--white)}
.welcome h2{left:78px;top:40px;font-family:'Raleway',sans-serif;font-weight:400;font-size:35px}
.welcome h2 span{color:var(--blue)}
.welcome p{left:78px;width:770px;font-size:15.5px;line-height:28px}
.welcome .read{left:78px;top:320px;font-size:17px;letter-spacing:1px;border-bottom:2px solid var(--white);padding-bottom:4px}
.welcome .mark{left:880px;top:126px;display:flex;align-items:center;gap:14px}
.welcome .mark i{display:block;width:104px;height:104px;background:var(--blue-dark)}
.welcome .mark b{font-size:32px;font-weight:700;color:var(--blue-dark)}
/* about */
.about{top:1171px;height:716px}
.about .title{position:absolute;top:30px;width:100%}
.about-item{left:78px;width:590px;height:112px}
.about-item .thumb{position:absolute;left:0;top:0;width:122px;height:100px}
.about-item h3{position:absolute;left:148px;top:0;font-size:18px;font-weight:400;color:var(--blue)}
.about-item p{position:absolute;left:148px;top:28px;width:440px;font-size:13.5px;line-height:19px;color:#555}
.about-item .more{position:absolute;left:148px;top:70px;font-size:13px;color:var(--blue-dark)}
.about .divider{left:676px;top:88px;width:1px;height:590px;background:var(--line)}
.about-video{left:712px;top:102px;width:374px;height:246px;background:linear-gradient(135deg,#dfe3e6,#f6f6f5 50%,#9aa3ab)}
.play{left:872px;top:196px;width:52px;height:52px;border-radius:50%;background:#111}
.about .lead{left:712px;top:366px;width:374px;font-size:15.5px;line-height:30px;color:#555}
.about .link-more{left:712px;top:580px;border-bottom:1px solid var(--line);padding:0 40px 8px 0}
/* strategy */
.strategy{top:1887px;height:792px;background:linear-gradient(180deg,#eef2f5,#e3e9ee 60%,#eef2f5)}
.strategy .title{position:absolute;top:30px;width:100%}
.strat{width:480px;height:110px}
.strat .icon{position:absolute;left:0;top:0;width:104px;height:104px;border-radius:50%;background:#bdc2c7;display:flex;align-items:center;justify-content:center}
.strat h3{position:absolute;left:133px;top:10px;width:345px;font-size:16px;font-weight:500;color:#222}
.strat p{position:absolute;left:133px;top:36px;width:345px;font-size:14px;line-height:20px;color:#555}
.strategy .view{left:528px;top:705px;font-size:19px;letter-spacing:1px;border-bottom:2px solid #222;padding:0 12px 4px}
/* services */
.services{top:2679px;height:433px;background:var(--blue);color:var(--white);text-align:center}
.services .title{position:absolute;top:38px;width:100%;color:var(--white)}
.svc{width:200px;top:112px}
.svc .circle{width:128px;height:128px;border-radius:50%;background:var(--white);margin:0 auto;display:flex;align-items:center;justify-content:center}
.svc h3{font-size:16px;font-weight:400;margin-top:20px}
.svc p{font-size:13.5px;line-height:19px;margin:8px auto 0;width:170px}
.services .read{left:530px;top:357px;font-size:19px;letter-spacing:1px;border-bottom:2px solid var(--white);padding-bottom:4px}
/* experience */
.experience{top:3112px;height:443px}
.experience .title{position:absolute;top:30px;width:100%}
.exp-photo{left:125px;top:102px;width:395px;height:236px;background:linear-gradient(135deg,#d9e1e8,#f2efe9 50%,#b5c2cc)}
.experience .cap{left:125px;top:350px;width:395px;font-size:13.5px;line-height:19px;color:#555;text-align:center}
.accordion{left:603px;top:102px;width:487px;border:1px solid var(--line)}
.acc-head{height:44px;border-bottom:1px solid var(--line);display:flex;align-items:center;gap:14px;padding-left:16px;font-size:16px;color:var(--blue-dark)}
.acc-head b{font-weight:700;font-size:20px;color:var(--blue)}
.acc-body{padding:10px 20px 14px 52px;font-size:13.5px;line-height:19px;color:#555;border-bottom:1px solid var(--line)}
.acc-head:last-child{border-bottom:0}
/* security */
.security{top:3555px;height:263px;background:linear-gradient(90deg,#0a4f7e,#0c5e94 60%,#0a4775);color:var(--white)}
.security h2{left:78px;top:38px;font-size:32px;font-weight:400;font-family:'Raleway',sans-serif}
.security p{left:78px;top:96px;width:790px;font-size:15.5px;line-height:29px}
.security .lock{left:912px;top:48px;width:168px;height:168px;border-radius:50%;border:6px solid var(--white);background:radial-gradient(circle at 40% 40%,#e1c66a,#6e6b63 60%,#2d3238)}
/* news */
.news{top:3818px;height:498px;background:linear-gradient(180deg,#ffffff,#f1f3f5)}
.news .title{position:absolute;top:36px;width:100%;font-size:40px}
.card{top:112px;width:325px}
.card .img{position:relative;height:210px;background:linear-gradient(135deg,#dde4ea,#f5f3ef 55%,#aeb9c3)}
.date{position:absolute;left:0;top:0;width:60px;height:60px;background:#1c1c1c;color:var(--white);text-align:center}
.date b{display:block;font-size:26px;font-weight:500;line-height:36px}
.date small{font-size:11px;text-transform:uppercase}
.card h3{font-size:15.5px;font-weight:400;color:var(--blue);margin-top:16px}
.card p{font-size:13.5px;line-height:19px;color:#555;margin-top:6px}
.card .more{font-size:13px;color:var(--blue-dark);margin-top:14px;display:block}
/* footer */
.footer{top:4316px;height:369px;background:var(--black);color:var(--white)}
.footer .brand{left:118px;top:48px;flex-direction:column;align-items:flex-start;gap:10px}
.footer .brand .brand-square{width:56px;height:56px;background:var(--blue)}
.footer .brand .brand-name{font-size:28px;color:var(--blue)}
.footer .about-text{left:78px;top:212px;width:250px;font-size:13.5px;line-height:20px}
.footer .rule{left:78px;top:268px;width:260px;height:1px;background:#444}
.footer .socials{left:100px;top:292px}
.footer .socials i{width:44px;height:44px;background:var(--blue)}
.footer h4{font-size:15px;font-weight:400;text-transform:uppercase;color:var(--blue);letter-spacing:1px}
.footer ul{list-style:none;font-size:14px;line-height:27px;margin-top:14px}
.footer ul li:first-child{color:var(--blue)}
.links{left:380px;top:44px}
.contact{left:576px;top:44px}
.contact .row{display:flex;gap:14px;font-size:14px;line-height:20px;margin-top:22px;align-items:flex-start}
.blogs{left:860px;top:44px}
.blogs h4{color:var(--white);text-transform:none;font-size:17px}
.blog-grid{display:grid;grid-template-columns:120px 120px;gap:20px;margin-top:20px}
.blog-grid div{height:104px;background:linear-gradient(135deg,#cfd8e0,#f0ede8 55%,#7f95a8)}
/* bottom */
.bottom{top:4685px;height:128px;background:var(--blue);color:var(--white)}
.subscribe{left:78px;top:40px;width:612px;height:56px;border-radius:28px;background:var(--white);display:flex;align-items:center;padding-left:28px;gap:14px;color:#333;font-size:17px}
.subscribe .btn{position:absolute;right:0;top:0;width:170px;height:56px;border-radius:28px;background:#0b0b0b;color:var(--white);display:flex;align-items:center;justify-content:center;font-size:16px;text-transform:uppercase}
.copy{left:900px;top:46px;font-size:13.5px;line-height:20px;text-transform:none}
</style>
</head>
<body>

<header class="section site-header">
  <div class="abs brand"><i class="brand-square"></i><span class="brand-name">Korvenza</span></div>
  <div class="abs top-links">
    <span>Live Chat <svg class="ico" width="20" height="16" viewBox="0 0 20 16"><path d="M2 1h16v10H8l-4 4v-4H2z" fill="#1a92d2"/></svg></span>
    <span>Email Us <svg class="ico" width="20" height="14" viewBox="0 0 20 14"><rect x="1" y="1" width="18" height="12" fill="#1a92d2"/><path d="M1 1l9 7 9-7" stroke="#fff" stroke-width="1.5" fill="none"/></svg></span>
    <span>How can we help <svg class="ico" width="22" height="14" viewBox="0 0 22 14"><path d="M1 7h16M12 2l6 5-6 5" stroke="#1a92d2" stroke-width="3" fill="none"/></svg></span>
    <span><svg width="30" height="30" viewBox="0 0 30 30" style="vertical-align:middle;margin-right:8px"><circle cx="15" cy="15" r="15" fill="#1a92d2"/><path d="M10 8l3 0 1 4-2 1.5a9 9 0 0 0 4.5 4.5L18 16l4 1v3c-7 1-13-5-12-12z" fill="#fff"/></svg>123-456-7890</span>
  </div>
  <div class="abs socials"><i></i><i></i><i></i><i></i></div>
</header>

<nav class="section main-nav">
  <a class="active">Home</a><a>About Us</a><a>Services</a><a>Strategy</a><a>Experience</a><a>Security</a><a>News</a><a>Contact Us</a>
</nav>

<section class="section hero">
  <div class="abs hero-photo" role="img" aria-label="Businessman in a suit standing at a balcony railing overlooking a city skyline"></div>
  <h1 class="abs">OUT SOURCING</h1>
  <h2 class="abs">BEST FOR YOUR BUSINESS</h2>
  <div class="abs btn-blue">Join Us Now</div>
</section>

<section class="section welcome">
  <h2 class="abs">Welcome To <span>Outsourcing Business Services</span></h2>
  <p class="abs" style="top:108px">Lorem Ipsum is simply dummy text of the printing and typesetting industry. Lorem Ipsum has been the industry's standard dummy text ever since the 1500s, when an unknown printer took a galley of type and scrambled it to make a type specimen book.</p>
  <p class="abs" style="top:220px">Lorem Ipsum is simply dummy text of the printing and typesetting industry. Lorem Ipsum has been the industry's standard dummy text ever since the 1500s.</p>
  <div class="abs read">READ MORE</div>
  <div class="abs mark"><i></i><b>Korvenza</b></div>
</section>

<section class="section about">
  <h2 class="title">About <span>Outsourcing Business</span></h2>
  <div class="abs about-item" style="top:90px"><div class="thumb" role="img" aria-label="City towers at dusk" style="background:linear-gradient(135deg,#6f8fae,#d6dde3)"></div><h3>Our Company</h3><p>Korvenza Staffing access to a large pool of employees with a wide range of skill sets.</p><span class="more">READ MORE</span></div>
  <div class="abs about-item" style="top:206px"><div class="thumb" role="img" aria-label="Person in a glowing blue space" style="background:linear-gradient(135deg,#0a1a4a,#2d6fd0)"></div><h3>Our Culture</h3><p>Korvenza Staffing access to a large pool of employees with a wide range of skill sets.</p><span class="more">READ MORE</span></div>
  <div class="abs about-item" style="top:322px"><div class="thumb" role="img" aria-label="Team member at an event" style="background:linear-gradient(135deg,#2a1f5a,#c2456a)"></div><h3>Our People</h3><p>The Philippines was ranked as the highest number of workers in grown annually every year by 46%.</p><span class="more">READ MORE</span></div>
  <div class="abs about-item" style="top:438px"><div class="thumb" role="img" aria-label="Group of colleagues together" style="background:linear-gradient(135deg,#5a3a2a,#d9a07a)"></div><h3>Our Story</h3><p>Our parent company is a leading e-commerce company with over 25 million in annual online sales.</p><span class="more">READ MORE</span></div>
  <div class="abs about-item" style="top:554px"><div class="thumb" role="img" aria-label="Office facility interior" style="background:linear-gradient(135deg,#8a2a2a,#d8c9b0)"></div><h3>Our Facilities</h3><p>Our Facility is equipped with the latest state technology, provide the tools needed for all agents to succeed.</p><span class="more">READ MORE</span></div>
  <div class="abs divider"></div>
  <div class="abs about-video" role="img" aria-label="Video still of a smiling professional with glasses at a desk"></div>
  <svg class="abs play" viewBox="0 0 52 52"><circle cx="26" cy="26" r="26" fill="#111"/><path d="M21 16l15 10-15 10z" fill="#fff"/></svg>
  <p class="abs lead">Outsourcing is a managed outsourcing service. We help businesses from around the world reduce overhead, complete projects and extend their companies overall output by providing a scalable workforce.</p>
  <div class="abs link-more">READ MORE</div>
</section>

<section class="section strategy">
  <h2 class="title">Our Strategy</h2>
  <div class="abs strat" style="left:78px;top:156px"><div class="icon"><svg width="50" height="40" viewBox="0 0 50 40" fill="#fff"><circle cx="12" cy="10" r="6"/><circle cx="38" cy="10" r="6"/><circle cx="25" cy="14" r="7"/><rect x="4" y="20" width="16" height="16" rx="4"/><rect x="30" y="20" width="16" height="16" rx="4"/><rect x="16" y="24" width="18" height="16" rx="4"/></svg></div><h3>Structured Hiring Process</h3><p>Procedure that ensures we hire only the best candidates for the job.</p></div>
  <div class="abs strat" style="left:78px;top:272px"><div class="icon"><svg width="48" height="48" viewBox="0 0 48 48"><circle cx="24" cy="24" r="12" fill="none" stroke="#fff" stroke-width="8" stroke-dasharray="6 4"/><circle cx="24" cy="24" r="5" fill="#fff"/></svg></div><h3>Optimizing Work Capacity</h3><p>The right people, providing all the necessary support, tools and technology.</p></div>
  <div class="abs strat" style="left:78px;top:388px"><div class="icon"><svg width="50" height="40" viewBox="0 0 50 40" fill="#fff"><path d="M4 4h32v20H16l-8 8v-8H4z"/><path d="M40 12h6v18h-4v6l-6-6H22v-4h18z"/></svg></div><h3>Centralized Customer Communication and Escalation</h3><p style="top:58px">Staff accounts supervisor and upper management only.</p></div>
  <div class="abs strat" style="left:78px;top:504px"><div class="icon"><svg width="40" height="50" viewBox="0 0 40 50" fill="#fff"><path d="M10 30l-4 18 14-8 14 8-4-18z"/><circle cx="20" cy="18" r="15"/><circle cx="20" cy="18" r="8" fill="#bdc2c7"/></svg></div><h3>Thorough Employee Vetting</h3><p>This involves a strenuous but worthy process of correctly selecting best fit members according to skill set.</p></div>
  <div class="abs strat" style="left:620px;top:156px"><div class="icon"><svg width="50" height="40" viewBox="0 0 50 40" fill="#fff"><path d="M2 18l12-10 10 6 12-6 12 10-14 14-10-6-8 6z"/></svg></div><h3>Business Critical and Zero Tolerance</h3><p>Identify business impacting Critical Errors and Zero Tolerance specifics.</p></div>
  <div class="abs strat" style="left:620px;top:272px"><div class="icon"><svg width="48" height="48" viewBox="0 0 48 48" fill="#fff"><circle cx="20" cy="14" r="8"/><path d="M4 42c0-12 8-18 16-18s12 4 14 8"/><circle cx="36" cy="36" r="7" fill="none" stroke="#fff" stroke-width="4"/></svg></div><h3>Skill Set Resiliency and Contingency</h3><p>Resource materials to Korvenza Staffing's Centralize Online Tool for quick reference.</p></div>
  <div class="abs strat" style="left:620px;top:388px"><div class="icon"><svg width="40" height="48" viewBox="0 0 40 48" fill="#fff"><path d="M4 2h22l10 10v34H4z"/><path d="M10 20h20M10 28h20M10 36h14" stroke="#bdc2c7" stroke-width="3"/></svg></div><h3>Quality Analysis and Review</h3><p>Quality Analyst form to ensure production standards are followed with consistency.</p></div>
  <div class="abs strat" style="left:620px;top:504px"><div class="icon"><svg width="46" height="46" viewBox="0 0 46 46"><rect x="3" y="5" width="34" height="36" fill="none" stroke="#fff" stroke-width="4"/><path d="M10 22l9 9 22-24" stroke="#fff" stroke-width="6" fill="none"/></svg></div><h3>Operational Standardization</h3><p>Primarily design to significantly minimize process variance and inconsistencies.</p></div>
  <div class="abs view">VIEW ALL</div>
</section>

<section class="section services">
  <h2 class="title">Our Best <span style="color:#fff">Services</span></h2>
  <div class="abs svc" style="left:80px"><div class="circle"><svg width="60" height="60" viewBox="0 0 60 60" fill="#1a92d2"><circle cx="30" cy="22" r="12"/><path d="M10 56c0-14 9-22 20-22s20 8 20 22z"/><path d="M14 24a16 16 0 0 1 32 0" fill="none" stroke="#1a92d2" stroke-width="4"/></svg></div><h3>Customer Service</h3><p>Lorem Ipsum simply dummy of the printing</p></div>
  <div class="abs svc" style="left:295px"><div class="circle"><svg width="62" height="56" viewBox="0 0 62 56" fill="none" stroke="#1a92d2" stroke-width="5"><path d="M2 4h10l8 30h32l6-22H16"/><circle cx="24" cy="48" r="4" fill="#1a92d2"/><circle cx="46" cy="48" r="4" fill="#1a92d2"/></svg></div><h3>Ecommerce</h3><p>Lorem Ipsum simply dummy of the printing</p></div>
  <div class="abs svc" style="left:505px"><div class="circle"><svg width="60" height="60" viewBox="0 0 60 60"><circle cx="30" cy="30" r="26" fill="#1a92d2"/><path d="M16 44L44 16M22 18l20 24" stroke="#fff" stroke-width="4"/></svg></div><h3>Creative</h3><p>Lorem Ipsum simply dummy of the printing</p></div>
  <div class="abs svc" style="left:715px"><div class="circle"><svg width="60" height="56" viewBox="0 0 60 56"><rect x="4" y="4" width="52" height="36" fill="#1a92d2"/><rect x="22" y="42" width="16" height="6" fill="#1a92d2"/><rect x="14" y="48" width="32" height="4" fill="#1a92d2"/><path d="M18 28l8-8 6 6 10-10" stroke="#fff" stroke-width="3" fill="none"/></svg></div><h3>IT Solutions</h3><p>Lorem Ipsum simply dummy of the printing</p></div>
  <div class="abs svc" style="left:930px"><div class="circle"><svg width="64" height="50" viewBox="0 0 64 50" fill="#1a92d2"><circle cx="32" cy="12" r="9"/><circle cx="12" cy="18" r="7"/><circle cx="52" cy="18" r="7"/><path d="M16 48c0-14 7-22 16-22s16 8 16 22z"/><path d="M0 46c0-10 5-16 12-16 3 0 5 1 7 3-3 4-4 8-4 13z"/><path d="M64 46c0-10-5-16-12-16-3 0-5 1-7 3 3 4 4 8 4 13z"/></svg></div><h3>Human Resources</h3><p>Lorem Ipsum simply dummy of the printing</p></div>
  <div class="abs read">READ MORE</div>
</section>

<section class="section experience">
  <h2 class="title"><span style="color:#1e1e1e">Our</span> <span>Experience</span></h2>
  <div class="abs exp-photo" role="img" aria-label="Team of colleagues gathered around a laptop in a meeting"></div>
  <p class="abs cap">Lorem Ipsum is simply dummy text of the printing and typesetting industry.</p>
  <div class="abs accordion">
    <div class="acc-head"><b>−</b>Why Outsource??</div>
    <div class="acc-body">Lorem Ipsum is simply dummy text of the printing and typesetting industry. Lorem Ipsum has been the industry's standard dummy text ever since the 1500s.</div>
    <div class="acc-head"><b>+</b>Benefits of Outsourcing?</div>
    <div class="acc-head"><b>+</b>Are you employees fully vetted?</div>
    <div class="acc-head"><b>+</b>Why Korvenza Staffing Solutions??</div>
  </div>
</section>

<section class="section security">
  <h2 class="abs">Security</h2>
  <p class="abs">Outsourcing uses state of the art biometric and proximity card access that is specific to every employee. We have a Zero Tolerance policy for tailgating and using other employee's access credentials. Our multiple close circuit cameras and remote monitoring on all entrances and exits ensure we have absolute visibility and record of all the activities in those areas.</p>
  <div class="abs lock" role="img" aria-label="Gold padlock on a keyboard"></div>
</section>

<section class="section news">
  <h2 class="title"><span style="color:#1e1e1e">Latest</span> <span>News</span></h2>
  <article class="abs card" style="left:78px"><div class="img" role="img" aria-label="Smiling call center agents wearing headsets"><div class="date"><b>14</b><small>May</small></div></div><h3>Lorem Ipsum is simply text Dummy</h3><p>Lorem Ipsum is simply dummy text of the printing and typesetting industry.</p><span class="more">READ MORE »</span></article>
  <article class="abs card" style="left:438px"><div class="img" role="img" aria-label="Business handshake across a desk"><div class="date"><b>26</b><small>Jan</small></div></div><h3>Lorem Ipsum is simply text Dummy</h3><p>Lorem Ipsum is simply dummy text of the printing and typesetting industry.</p><span class="more">READ MORE »</span></article>
  <article class="abs card" style="left:798px"><div class="img" role="img" aria-label="Team of office workers at computers"><div class="date"><b>15</b><small>Sep</small></div></div><h3>Lorem Ipsum is simply text Dummy</h3><p>Lorem Ipsum is simply dummy text of the printing and typesetting industry.</p><span class="more">READ MORE »</span></article>
</section>

<footer class="section footer">
  <div class="abs brand"><i class="brand-square"></i><span class="brand-name">Korvenza</span></div>
  <p class="abs about-text">Lorem Ipsum is simply dummy text of the printing and typeing</p>
  <div class="abs rule"></div>
  <div class="abs socials"><i></i><i></i><i></i></div>
  <div class="abs links"><h4>Useful Links</h4><ul><li>Home</li><li>About</li><li>Services</li><li>Strategy</li><li>Experience</li><li>Security</li><li>News</li><li>Contact Us</li></ul></div>
  <div class="abs contact"><h4>Contact Us</h4>
    <div class="row"><svg width="18" height="24" viewBox="0 0 18 24"><path d="M9 0a9 9 0 0 1 9 9c0 6-9 15-9 15S0 15 0 9a9 9 0 0 1 9-9z" fill="#1a92d2"/><circle cx="9" cy="9" r="3" fill="#000"/></svg><span>125,Building Name,Street,<br>City,Country-Zipcode</span></div>
    <div class="row"><svg width="20" height="20" viewBox="0 0 20 20"><path d="M3 1h4l1 5-2 2a11 11 0 0 0 6 6l2-2 5 1v4c-10 1-17-6-16-16z" fill="#1a92d2"/></svg><span>123-456-7890</span></div>
    <div class="row"><svg width="22" height="16" viewBox="0 0 22 16"><rect x="1" y="1" width="20" height="14" fill="#1a92d2"/><path d="M1 1l10 8 10-8" stroke="#000" stroke-width="1.5" fill="none"/></svg><span>info@korvenzaservices.com</span></div>
  </div>
  <div class="abs blogs"><h4>Latest Blogs</h4>
    <div class="blog-grid"><div role="img" aria-label="Colleagues shaking hands"></div><div role="img" aria-label="Hands joined together"></div><div role="img" aria-label="Business meeting"></div><div role="img" aria-label="Team discussion"></div></div>
  </div>
</footer>

<section class="section bottom">
  <div class="abs subscribe"><svg width="22" height="16" viewBox="0 0 22 16"><rect x="1" y="1" width="20" height="14" fill="none" stroke="#333" stroke-width="1.6"/><path d="M1 1l10 8 10-8" stroke="#333" stroke-width="1.6" fill="none"/></svg>Email<span class="btn">Subscribe!</span></div>
  <p class="abs copy">© &nbsp;OUT SOURCE SERVICES<br>2016. All Rights Reserved.</p>
</section>

</body>
</html>
```